Occupational Medical Billing and Coding Business needs Postcard

Medical billing and coding business needs marketing postcard to send to target audience of orthopaedic surgeons who practice medicine in California Workers' Compensation industry. These doctors treat injured workers and/or provide medical-legal evaluations and reports for the courts to settle the injured worker's claim. This is a highly specialized area of medical billing and coding. It is extremely complicated and can be very frustrating for doctors and their staff who do not understand the system. I would encourage the designers to check out my website: www.CorvaleHealthClaims.com
I want something bright and colorful that makes bold statements. It has to get their attention. My suggestions for bold statements include:
1) QMEs! Are your bills compliant with DWC's view? We make sure your complexity factors are maximized as well as compliant.
2) We collected over $ 462,000 just in second bill review (SBR) appeals alone and that's just one orthopaedic surgeon! Imagine what we can do for you!

I uploaded a word document with some information about the services I offer. The company logo is also there. Let me know if you need it in another format. The items with the asterisk (**) must be in the postcard.

Thank you so much!

Corvale Health Claims

Target Market(s)

Orthopaedic Surgeons who treat injured workers in California

Font styles to use
Sans Serif

Colors

Designer to choose colors to be used in the design.

Requirements
Must have
• Expert Billing and Coding Services for:
• QME - AME - IME Evaluations
• Radiology - MRI/CT Scans
• Orthopaedic Surgery
• Certified Coders on Staff
• Electronic Claim Submission
• Payment within 15 days
• It's important to spell orthopaedic with the "A" after the "P" as it is an acknowledgment of the origins of the practice and will attract a doctor with higher education.

```html
<!DOCTYPE html>
<html lang="en">
<head>
<meta charset="utf-8">
<title>Corvale Health Claims – Postcard</title>
<link rel="stylesheet" href="https://fonts.googleapis.com/css2?family=Questrial&family=Raleway:wght@500;600;700&display=swap">
<style>
  :root {
    --page: #ffffff;
    --navy: #23233f;
    --slate: #2f3856;
    --slate-soft: #4b5677;
    --royal: #4b86cf;
    --sky: #a6c4e8;
    --white: #ffffff;
    --ink: #2a2d3e;
    --badge: #2f8fd8;
  }
  * { box-sizing: border-box; margin: 0; padding: 0; }
  html, body { width: 796px; height: 1200px; overflow: hidden; background: var(--page); }
  body { position: relative; font-family: "Questrial", sans-serif; }

  .card { position: absolute; left: 28px; width: 740px; overflow: hidden; }
  .card--front { top: 16px; height: 572px; background: var(--royal); }
  .card--back { top: 606px; height: 578px; background: var(--sky); }

  /* front */
  .hero-photo {
    position: absolute; left: 0; top: 0; width: 740px; height: 342px;
    background: linear-gradient(100deg, #f4f3f1 0%, #e9e7e4 38%, #d9dde3 62%, #b9c4cf 82%, #8e9aa6 100%);
  }
  .hero-copy { position: absolute; left: 30px; top: 40px; width: 370px; text-align: center; color: var(--slate); }
  .hero-title { font-family: "Raleway", sans-serif; font-weight: 700; font-size: 30px; line-height: 36px; }
  .hero-question { font-family: "Raleway", sans-serif; font-weight: 600; font-size: 22px; line-height: 28px; margin-top: 2px; }
  .hero-question em { font-style: italic; }
  .hero-promise { font-size: 20px; line-height: 26px; color: var(--slate-soft); margin-top: 8px; }
  .hero-url {
    position: absolute; left: 48px; top: 278px;
    font-family: "Raleway", sans-serif; font-weight: 700; font-size: 13px; letter-spacing: .3px; color: var(--navy);
  }
  .service-band {
    position: absolute; left: 0; top: 342px; width: 740px; height: 39px; background: var(--navy);
    color: var(--white); font-family: "Raleway", sans-serif; font-weight: 600; font-size: 16px;
    font-variant: small-caps; letter-spacing: .2px; display: flex; align-items: center; justify-content: center;
  }
  .brand-name--front {
    position: absolute; left: 40px; top: 440px; width: 340px;
    color: var(--white); font-family: "Questrial", sans-serif; font-size: 36px; line-height: 42px;
  }
  .service-list { position: absolute; left: 420px; top: 418px; list-style: none; color: #eef3fb; font-size: 18px; line-height: 24px; }
  .service-list li::before, .perk-list li::before { content: "\2713"; margin-right: 7px; font-size: .85em; }

  /* back */
  .brand-name--back {
    position: absolute; left: 40px; top: 54px; width: 360px;
    color: var(--navy); font-family: "Questrial", sans-serif; font-size: 32px; line-height: 38px;
  }
  .perk-list { position: absolute; left: 36px; top: 156px; list-style: none; color: var(--ink); font-size: 16px; line-height: 27px; }
  .perk-list .indent { padding-left: 20px; display: block; line-height: 20px; margin-top: -4px; }
  .contact-badge { position: absolute; left: 118px; top: 332px; }
  .contact-lines { position: absolute; left: 40px; top: 416px; color: var(--ink); }
  .contact-line { display: flex; align-items: center; gap: 12px; }
  .contact-line svg { flex: none; }
  .contact-phone { font-size: 25px; height: 34px; }
  .contact-small {
    font-family: "Raleway", sans-serif; font-weight: 700; font-size: 14px; font-variant: small-caps;
    letter-spacing: .3px; height: 26px;
  }
</style>
</head>
<body>

<section class="card card--front">
  <div class="hero-photo" role="img" aria-label="Photo of a hand using a calculator on a desk with glasses, laptop and stethoscope"></div>
  <div class="hero-copy">
    <h1 class="hero-title">QMEs!</h1>
    <p class="hero-question">Are your bills <em>compliant</em><br>with DWC's view?</p>
    <p class="hero-promise">We make sure your complexity factors are maximized as well as compliant!</p>
  </div>
  <p class="hero-url">WWW.CORVALEHEALTHCLAIMS.COM</p>
  <div class="service-band">Expert Billing and Coding Services for Workers' Compensation Providers</div>
  <p class="brand-name--front">Corvale Health Claims</p>
  <ul class="service-list">
    <li>QME – AME – IME Evaluations</li>
    <li>Radiology – MRI/CT Scans</li>
    <li>Electrodiagnostic Studies</li>
    <li>Orthopaedic Surgery</li>
    <li>Ambulatory Surgery Centers</li>
  </ul>
</section>

<section class="card card--back">
  <p class="brand-name--back">Corvale Health Claims</p>
  <ul class="perk-list">
    <li>Certified Coders on Staff</li>
    <li>Electronic Claim Submission</li>
    <li>Payment within 15 days</li>
    <li>Over 25 Years Experience<span class="indent">in Workers' Comp</span></li>
    <li>We also provide Collection Services!</li>
  </ul>

  <svg class="contact-badge" width="124" height="72" viewBox="0 0 124 72" aria-label="Contact us">
    <defs>
      <linearGradient id="badgeFill" x1="0" y1="0" x2="0" y2="1">
        <stop offset="0" stop-color="#5db3ee"/>
        <stop offset="1" stop-color="#1f7cc9"/>
      </linearGradient>
    </defs>
    <path d="M4 6 L120 2 L118 52 L84 54 L78 70 L68 55 L6 58 Z" fill="url(#badgeFill)"/>
    <text x="62" y="36" text-anchor="middle" fill="#ffffff" font-family="Raleway, sans-serif" font-weight="700" font-size="20" transform="rotate(-2 62 30)">contact us</text>
  </svg>

  <div class="contact-lines">
    <div class="contact-line contact-phone">
      <svg width="18" height="18" viewBox="0 0 18 18" aria-hidden="true">
        <circle cx="9" cy="9" r="8" fill="none" stroke="#2f6fb8" stroke-width="1.5"/>
        <path d="M6.5 5 q-1 4 3 8 l1.5-1.5 -1.6-1.6 -1 .8 q-1.6-1.6-1.3-3.3 l1-.7 -1-2.2z" fill="#2f6fb8"/>
      </svg>
      <span>555. 014.2290</span>
    </div>
    <div class="contact-line contact-small">
      <svg width="18" height="14" viewBox="0 0 18 14" aria-hidden="true">
        <rect x="1" y="2" width="16" height="11" fill="none" stroke="#2f6fb8" stroke-width="1.3"/>
        <path d="M1 2 L9 8 L17 2" fill="none" stroke="#2f6fb8" stroke-width="1.3"/>
      </svg>
      <span>info@CorvaleHealthClaims.com</span>
    </div>
    <div class="contact-line contact-small">
      <svg width="18" height="18" viewBox="0 0 18 18" aria-hidden="true">
        <circle cx="9" cy="9" r="7.5" fill="none" stroke="#2f6fb8" stroke-width="1.3"/>
        <ellipse cx="9" cy="9" rx="3.3" ry="7.5" fill="none" stroke="#2f6fb8" stroke-width="1.1"/>
        <path d="M1.5 9 H16.5 M3 5 H15 M3 13 H15" stroke="#2f6fb8" stroke-width="1.1"/>
      </svg>
      <span>www.CorvaleHealthClaims.com</span>
    </div>
  </div>
</section>

</body>
</html>
```